Harborline Portable Scans
Mobile Ultrasound
Every draft has been amazing. I didn't really understand that a small business card could be designed with so much artistry and imagination. Thanks to all who participated in this for us. Unfortunately, we can only pick one. I'm going to do that now. Thanks again to all! --Dale
THIS IS REALLY IMPORTANT!! Seems like I now have a new phone number! Please change the phone number on the card to 555.318.4426 on all drafts.
Thank You!
Thanks for all the FANTASTIC drafts! We've decided on a one sided card. Also, to my knowledge, all the logo formats should have been downloaded. I don't know how to upload an .ai file...I can contact someone at MarkSmith tomorrow to see if this can be done.
LOGO file has been uploaded!
--- Gerald
You wrote single-sided, but then wrote that you wanted your logo on the backside. Does that mean you want a double sided card? :)
Can you please upload an .ai file with the logo?

```html
<!DOCTYPE html>
<html lang="en">
<head>
<meta charset="utf-8">
<title>Harborline Portable Scans — Business Card</title>
<link rel="stylesheet" href="https://fonts.googleapis.com/css2?family=Source+Sans+3:wght@400;600;700&display=swap">
<style>
  :root {
    --maroon: #8a1538;
    --maroon-deep: #5e0a25;
    --maroon-light: #b24a69;
    --swoosh-gray: #b9b9bb;
    --ink: #1d1d1f;
    --frame: #d4d4d4;
    --card-edge: #3a3a3a;
    --paper: #ffffff;
  }
  * { box-sizing: border-box; margin: 0; padding: 0; }
  html, body { width: 1200px; height: 643px; overflow: hidden; background: var(--paper); }
  body { font-family: "Source Sans 3", "Helvetica Neue", Arial, sans-serif; position: relative; }

  .presentation-frame {
    position: absolute; left: 28px; top: 28px; width: 1144px; height: 587px;
    border: 2px solid var(--frame);
  }

  .card {
    position: absolute; top: 190px; width: 480px; height: 283px;
    border: 1.5px solid var(--card-edge); border-radius: 14px; overflow: hidden;
  }
  .card-front { left: 96px; background: var(--paper); }
  .card-back {
    left: 606px; width: 490px;
    background: linear-gradient(90deg, var(--maroon-deep) 0%, var(--maroon) 55%, var(--maroon-light) 100%);
    display: flex; flex-direction: column; align-items: center; justify-content: center;
  }

  .wave { position: absolute; left: 0; top: 0; width: 100%; height: 100%; }

  .brand-front {
    position: absolute; left: 30px; top: 22px;
    display: flex; flex-direction: column; align-items: flex-start;
  }
  .brand-dot { width: 20px; height: 20px; border-radius: 50%; background: var(--maroon); margin: 0 0 6px 44px; }
  .brand-name-front {
    color: var(--maroon); font-weight: 600; font-size: 15px; line-height: 1.1;
    letter-spacing: 0.5px; text-transform: uppercase;
  }

  .holder { position: absolute; left: 296px; top: 24px; color: var(--ink); }
  .holder-name { font-weight: 700; font-size: 13px; }
  .holder-title { font-weight: 400; font-size: 11px; margin-top: 1px; }

  .contact-list {
    position: absolute; left: 28px; top: 160px; list-style: none;
    color: var(--paper); font-size: 9.5px; line-height: 13px;
  }

  .brand-dot-large { width: 46px; height: 46px; border-radius: 50%; background: var(--paper); margin-bottom: 14px; }
  .brand-name-back {
    color: var(--paper); font-weight: 600; font-size: 30px; line-height: 1.1;
    letter-spacing: 2px; text-transform: uppercase; text-align: center;
  }
</style>
</head>
<body>
  <div class="presentation-frame"></div>

  <section class="card card-front">
    <svg class="wave" viewBox="0 0 480 283" preserveAspectRatio="none" aria-hidden="true">
      <defs>
        <linearGradient id="band-fill" x1="0" y1="0" x2="1" y2="0">
          <stop offset="0" stop-color="#6e0f2e"/>
          <stop offset="0.6" stop-color="#8a1538"/>
          <stop offset="1" stop-color="#a83a5a"/>
        </linearGradient>
      </defs>
      <path d="M0,112 C160,128 310,196 480,150 L480,283 L0,283 Z" fill="var(--swoosh-gray)"/>
      <path d="M0,142 C170,160 320,216 480,174 L480,283 L0,283 Z" fill="url(#band-fill)"/>
    </svg>

    <div class="brand-front">
      <span class="brand-dot"></span>
      <span class="brand-name-front">Harborline<br>Portable Scans</span>
    </div>

    <div class="holder">
      <p class="holder-name">Nathan Corwell, D.C.</p>
      <p class="holder-title">Executive Director</p>
    </div>

    <ul class="contact-list">
      <li>P.O. Box 218</li>
      <li>Fernwood Falls, MI 49001</li>
      <li>Phone 555.318.4426</li>
      <li>Fax 555.204.7790</li>
      <li>Email: ncorwell@harborlineportablescans.com</li>
      <li>www.harborlineportablescans.com</li>
    </ul>
  </section>

  <section class="card card-back">
    <span class="brand-dot-large"></span>
    <span class="brand-name-back">Harborline<br>Portable Scans</span>
  </section>
</body>
</html>
```